Powerpoint design for management consultant

We need a powerpoint design to use for our corporate presentations, proposal summaries and for delivering report recommendations.

Target Market(s)

Executives in Government & Private Industry

Industry/Entity Type

Consultant

Requirements
Must have
• Must use the company logo contained in the uploaded files.
Must be a powerpoint template file (.potx) that can be used with Powerpoint 2007 and later.
Must have a title slide.
Must have a purpose slide (in today's presentation we will cover ....)
Must have an agenda slide.
Must have three topic slides (topic1, topic2, topic3) as transition slides
Must support side by side comparisons
Any images used must be available royalty/ license free
Must have a summary slide.
Must have a questions slide at the end.
Must have a footer containing slide number in format of x of y.
Must have a footer containing presentation name.
Must have a footer containing the presentation date.
Must have a footer containing "confidential"
Nice to have
• The powerpoint should support the ability to represent data using infographics.
Should not have
• no tag lines or references to being management consultants. must not use custom fonts.

```html
<!DOCTYPE html>
<html lang="en">
<head>
<meta charset="utf-8">
<title>Presentation Template Overview</title>
<link href="https://fonts.googleapis.com/css2?family=Open+Sans:wght@300;400;700;800&display=swap" rel="stylesheet">
<style>
:root{
  --band:#f2b98a;
  --orange:#e8873a;
  --orange-dark:#c8601c;
  --navy:#2b3d4f;
  --cal-line:#3b5a7a;
  --ink:#4a4a4a;
  --muted:#8a8a8a;
  --bg:#ffffff;
}
*{box-sizing:border-box;margin:0;padding:0}
html,body{width:1200px;height:1000px;overflow:hidden;background:var(--bg)}
body{position:relative;font-family:"Open Sans",sans-serif;color:var(--ink)}
.slide{position:absolute;width:280px;height:208px;overflow:hidden;background:#fff}
.band{position:absolute;background:var(--band);color:#5a4130;font-weight:300;font-size:11px;line-height:19px;padding-left:12px}
.footer{position:absolute;z-index:5;left:0;right:0;bottom:0;height:16px;font-size:5.5px;color:var(--muted);display:flex;align-items:center;padding:0 4px}
.footer span{margin-right:22px}
.footer .brand{margin-left:auto;margin-right:4px;font-weight:800;font-size:12px;letter-spacing:.5px;color:var(--navy)}
.footer .page{margin-right:0}
.fill{position:absolute}
.body-text{position:absolute;font-size:6.5px;line-height:9px;color:var(--ink)}
.brand-mark{position:absolute;font-weight:800;color:var(--navy);letter-spacing:2px}
.calendar{position:absolute;left:105px;top:56px;width:165px;display:grid;grid-template-columns:repeat(7,1fr);font-size:4.5px;color:#777}
.calendar .day-name{background:#eee;text-align:center;height:6px;line-height:6px}
.calendar .cell{height:19px;border-left:1.5px solid var(--cal-line);padding:3px 0 0 6px;margin-top:2px}
.calendar .cell.empty{border-left-color:transparent}
</style>
</head>
<body>

<!-- Title slide -->
<section class="slide" style="left:5px;top:100px">
  <div class="brand-mark" style="left:45px;top:126px;font-size:40px;opacity:.12">NORVALE</div>
  <div class="band" style="left:49px;top:14px;width:231px;height:31px;line-height:31px;font-size:12px;padding-left:18px">Insert your title here</div>
  <div class="band" style="left:82px;top:53px;width:198px;height:17px;line-height:17px;font-size:8px;padding-left:18px">possible subtitle</div>
  <div class="band" style="left:0;top:106px;width:117px;height:18px;line-height:18px;font-size:8px">Name</div>
  <div class="band" style="left:0;top:131px;width:117px;height:18px;line-height:18px;font-size:8px">Date</div>
  <div class="brand-mark" style="left:0;top:172px;font-size:28px">NORVALE</div>
</section>

<!-- Pro / contra slide -->
<section class="slide" style="left:305px;top:100px">
  <div class="band" style="left:0;top:10px;width:265px;height:20px;padding-left:52px">Editable graphs</div>
  <div class="fill" style="left:0;top:95px;width:280px;height:100px;background:linear-gradient(#fff,#d9d9d9)"></div>
  <div class="fill" style="left:10px;top:40px;width:128px;height:60px;border:1px solid #ccc;background:#fff">
    <div style="background:linear-gradient(#f4f4f4,#c8c8c8);font-size:6px;font-weight:700;padding:2px 4px">Pro Arguments</div>
    <div style="font-size:5.5px;line-height:10px;padding:2px 4px">• Argument 1<br>• Argument 2<br>• Argument 3<br>• Argument 4</div>
  </div>
  <div class="fill" style="left:142px;top:40px;width:128px;height:60px;border:1px solid #ccc;background:#fff">
    <div style="background:linear-gradient(#8a8a8a,#4a4a4a);color:#fff;font-size:6px;font-weight:700;padding:2px 4px">Contra Arguments</div>
    <div style="font-size:5.5px;line-height:10px;padding:2px 4px">• Argument 1<br>• Argument 2<br>• Argument 3<br>• Argument 4</div>
  </div>
  <svg class="fill" style="left:0;top:0" width="280" height="208" viewBox="0 0 280 208">
    <polygon points="150,118 230,118 242,126 230,134 150,134" fill="#6b6b6b"/>
    <polygon points="40,132 100,130 100,122 122,138 100,156 100,148 28,150" fill="#8e8e8e"/>
    <text x="52" y="145" font-size="9" fill="#fff" font-family="Open Sans, sans-serif">advantages</text>
    <text x="158" y="129" font-size="6" fill="#eee" font-family="Open Sans, sans-serif">disadvantages</text>
  </svg>
  <div class="body-text" style="left:196px;top:148px;width:80px;font-size:4.5px;line-height:6px;color:#888">This slide shows a pro/contra list of arguments for and against some topic or concept</div>
  <div class="footer"><span>23-Oct-13</span><span>Confidential</span><span>Presentation name</span><span class="brand">NORVALE</span><span class="page">22</span></div>
</section>

<!-- Abstract message slide -->
<section class="slide" style="left:607px;top:100px">
  <div class="fill" role="img" aria-label="Aged paper background texture" style="inset:0;background:radial-gradient(ellipse at 50% 45%,#e3c98d,#c49a55 80%,#a67b3e)"></div>
  <div class="band" style="left:107px;top:28px;width:173px;height:19px;background:var(--orange);color:#4a2a10;padding-left:16px">Abstract Message 3</div>
  <div class="body-text" style="left:14px;top:84px;width:260px;font-size:7.5px;line-height:12px;color:#5a3d1a">In engineering parlance the term aluminium covers any aluminium-based material, and embraces the alloys as well as the pure metal.</div>
  <div class="footer" style="color:#4a3520"><span>23-Oct-13</span><span>Confidential</span><span>Presentation name</span><span class="brand">NORVALE</span><span class="page">18</span></div>
</section>

<!-- Cycle diagram slide -->
<section class="slide" style="left:907px;top:100px">
  <div class="band" style="left:0;top:10px;width:265px;height:20px">Editable graphs</div>
  <div class="fill" style="left:0;top:75px;width:280px;height:60px;background:linear-gradient(#fff,#e6e6e6,#fff)"></div>
  <svg class="fill" style="left:0;top:0" width="280" height="208" viewBox="0 0 280 208">
    <ellipse cx="135" cy="112" rx="72" ry="30" fill="none" stroke="#e8873a" stroke-width="18"/>
    <path d="M63 112 A72 30 0 0 1 125 82" fill="none" stroke="#a4460e" stroke-width="18"/>
    <polygon points="200,128 222,118 214,140" fill="#e8873a"/>
  </svg>
  <div class="body-text" style="left:142px;top:56px;width:70px;font-size:5px;line-height:7px">This text can be replaced with your own text</div>
  <div class="body-text" style="left:8px;top:97px;width:45px;font-size:5px;line-height:7px">This text can be replaced with your own text</div>
  <div class="body-text" style="left:232px;top:135px;width:48px;font-size:5px;line-height:7px;color:var(--orange)">This text can be replaced with your own text</div>
  <div class="footer"><span>23-Oct-13</span><span>Confidential</span><span>Presentation name</span><span class="brand">NORVALE</span><span class="page">21</span></div>
</section>

<!-- Notes slide -->
<section class="slide" style="left:5px;top:347px">
  <div class="fill" role="img" aria-label="Graph paper background" style="inset:0;background:#eef5f9;border:1px solid #cfe1ea"></div>
  <div class="fill" style="left:0;top:30px;width:280px;height:1px;background:#e3a3a3"></div>
  <div class="body-text" style="left:42px;top:14px;font-size:9px;line-height:12px">Notes</div>
  <div class="body-text" style="left:42px;top:64px;width:200px;font-size:6px;line-height:8px;text-align:justify">In todays presentation we will cover "Structural Aluminium". In engineering parlance the term aluminium (or aluminium) covers any aluminium-based material, and embraces the alloys as well as the pure metal.</div>
  <div class="footer"><span>23-Oct-13</span><span>Confidential</span><span>Presentation name</span><span class="brand">NORVALE</span><span class="page">20</span></div>
</section>

<!-- Important message 2 -->
<section class="slide" style="left:305px;top:347px">
  <div class="fill" role="img" aria-label="Photo of people walking across a sunlit plaza" style="inset:0;background:radial-gradient(ellipse at 25% 35%,#f5a640,#c8601c 50%,#5a2408)"></div>
  <div class="band" style="left:102px;top:29px;width:124px;height:19px;background:rgba(200,110,40,.85);color:#fff;padding-left:8px">Important message 2</div>
  <div class="fill" style="left:54px;top:97px;width:226px;height:62px;background:rgba(120,45,10,.55)"></div>
  <div class="body-text" style="left:82px;top:110px;width:190px;font-size:6px;line-height:8.5px;color:#f7e3cd">In todays presentation we will cover "Structural Aluminium". In engineering parlance the term aluminium (or aluminium) covers any aluminium-based material, and embraces the alloys as well as the pure metal.</div>
  <div class="footer" style="color:#f3e3cf"><span>23-Oct-13</span><span>Confidential</span><span>Presentation name</span><span class="brand">NORVALE</span><span class="page">17</span></div>
</section>

<!-- Table slide -->
<section class="slide" style="left:607px;top:347px">
  <div class="band" style="left:0;top:10px;width:237px;height:20px">Table Presentation</div>
  <table class="fill" style="left:48px;top:43px;width:189px;border-collapse:collapse;font-size:5.5px;text-align:center">
    <tr style="background:var(--orange);color:#fff;font-size:9px;height:16px"><td>↑</td><td>↓</td></tr>
    <tr style="background:#f8d4b4;height:10px"><td>dsh</td><td>fshfsg</td></tr>
    <tr style="background:#f3c29c;height:10px"><td>adhah</td><td>sdgds</td></tr>
    <tr style="background:#f8d4b4;height:10px"><td>sdgs</td><td>fdsgh</td></tr>
    <tr style="background:#f3c29c;height:10px"><td>dsgs</td><td>sdgsfas</td></tr>
    <tr style="background:#f8d4b4;height:10px"><td>SGsd</td><td>sdgsdg</td></tr>
    <tr style="background:#f3c29c;height:10px"><td>DGSDG</td><td>sdgsdg</td></tr>
    <tr style="background:#f8d4b4;height:10px"><td>SGS</td><td>sdgsdg</td></tr>
  </table>
  <div class="band" style="left:48px;top:155px;width:232px;height:19px"></div>
  <div class="footer"><span>23-Oct-13</span><span>Confidential</span><span>Presentation name</span><span class="brand">NORVALE</span><span class="page">14</span></div>
</section>

<!-- Bar chart slide -->
<section class="slide" style="left:907px;top:347px">
  <div class="band" style="left:0;top:10px;width:141px;height:20px">Graphical Presentation</div>
  <svg class="fill" style="left:0;top:0" width="280" height="208" viewBox="0 0 280 208" font-family="Open Sans, sans-serif" font-size="6" fill="#555">
    <g stroke="#ddd" stroke-width=".5">
      <line x1="62" y1="150" x2="262" y2="150"/><line x1="62" y1="140" x2="262" y2="140"/>
      <line x1="62" y1="130" x2="262" y2="130"/><line x1="62" y1="120" x2="262" y2="120"/>
      <line x1="62" y1="110" x2="262" y2="110"/><line x1="62" y1="100" x2="262" y2="100"/>
      <line x1="62" y1="90" x2="262" y2="90"/><line x1="62" y1="80" x2="262" y2="80"/>
      <line x1="62" y1="70" x2="262" y2="70"/><line x1="62" y1="60" x2="262" y2="60"/>
    </g>
    <g text-anchor="end">
      <text x="56" y="152">0</text><text x="56" y="142">0.5</text><text x="56" y="132">1</text>
      <text x="56" y="122">1.5</text><text x="56" y="112">2</text><text x="56" y="102">2.5</text>
      <text x="56" y="92">3</text><text x="56" y="82">3.5</text><text x="56" y="72">4</text><text x="56" y="62">4.5</text>
    </g>
    <g fill="#d8661c">
      <rect x="92" y="64" width="10" height="86"/><rect x="137" y="99" width="10" height="51"/>
      <rect x="183" y="80" width="10" height="70"/><rect x="229" y="60" width="10" height="90"/>
    </g>
    <g text-anchor="middle">
      <text x="97" y="163">Category 1</text><text x="142" y="163">Category 2</text>
      <text x="188" y="163">Category 3</text><text x="234" y="163">Category 4</text>
    </g>
  </svg>
  <div class="footer"><span>23-Oct-13</span><span>Confidential</span><span>Presentation name</span><span class="brand">NORVALE</span><span class="page">12</span></div>
</section>

<!-- Important message 1 -->
<section class="slide" style="left:5px;top:600px">
  <div class="band" style="left:106px;top:15px;width:174px;height:19px;padding-left:16px">Important message 1</div>
  <div class="fill" role="img" aria-label="Illustration of an empty boardroom table with chairs" style="left:30px;top:66px;width:200px;height:124px;background:linear-gradient(180deg,#f1f1f1,#bdbdbd)"></div>
  <div class="fill" style="left:279px;top:0;width:1px;height:208px;background:#ccc"></div>
  <div class="footer"><span>23-Oct-13</span><span>Confidential</span><span>Presentation name</span><span class="brand">NORVALE</span><span class="page">15</span></div>
</section>

<!-- Agenda calendar slide -->
<section class="slide" style="left:305px;top:600px">
  <div class="band" style="left:0;top:7px;width:138px;height:19px">agenda</div>
  <div class="body-text" style="left:190px;top:38px;font-size:8px;color:#666">November 2013</div>
  <div class="calendar">
    <div class="day-name">Sun</div><div class="day-name">Mon</div><div class="day-name">Tue</div><div class="day-name">Wed</div><div class="day-name">Thu</div><div class="day-name">Fri</div><div class="day-name">Sat</div>
    <div class="cell empty"></div><div class="cell empty"></div><div class="cell empty"></div><div class="cell empty"></div><div class="cell empty"></div><div class="cell">1</div><div class="cell">2</div>
    <div class="cell">3</div><div class="cell">4</div><div class="cell">5</div><div class="cell">6</div><div class="cell">7</div><div class="cell">8</div><div class="cell">9</div>
    <div class="cell">10</div><div class="cell">11</div><div class="cell">12</div><div class="cell">13</div><div class="cell">14</div><div class="cell">15</div><div class="cell">16</div>
    <div class="cell">17</div><div class="cell">18</div><div class="cell">19</div><div class="cell">20</div><div class="cell">21</div><div class="cell">22</div><div class="cell">23</div>
    <div class="cell">24</div><div class="cell">25</div><div class="cell">26</div><div class="cell">27</div><div class="cell">28</div><div class="cell">29</div><div class="cell">30</div>
  </div>
  <svg class="fill" style="left:0;top:0" width="280" height="208" viewBox="0 0 280 208">
    <g fill="none" stroke="#e8873a" stroke-width=".9">
      <circle cx="137" cy="88" r="7"/><circle cx="160" cy="130" r="7"/>
      <line x1="94" y1="62" x2="130" y2="86"/><line x1="94" y1="140" x2="153" y2="131"/>
    </g>
    <polygon points="92,60 99,61 95,65" fill="#e8873a"/>
    <polygon points="92,140 97,136 98,141" fill="#e8873a"/>
  </svg>
  <div class="body-text" style="left:8px;top:48px;width:82px;font-size:4.5px;line-height:6px;text-align:justify">Pure aluminium is weak, with a tensile strength ranging from about 90 to 140 N/mm² depending on the temper.</div>
  <div class="body-text" style="left:8px;top:132px;width:82px;font-size:4.5px;line-height:6px;text-align:justify">It is employed for electrical conductors and for domestic products, but for serious structural use it has to be strengthened by alloying.</div>
  <div class="footer"><span>23-Oct-13</span><span>Confidential</span><span>Presentation name</span><span class="brand">NORVALE</span><span class="page">5</span></div>
</section>

<!-- Topic transition slide -->
<section class="slide" style="left:607px;top:600px">
  <div class="fill" role="img" aria-label="Cardboard texture background" style="inset:0;background:radial-gradient(ellipse at 50% 50%,#d8d0c4,#b9ae9e)"></div>
  <div class="fill" style="left:10px;top:60px;width:62px;height:62px;border:3px solid #222"></div>
  <div class="fill" style="left:78px;top:60px;width:62px;height:62px;border:3px solid #222"></div>
  <div class="fill" style="left:142px;top:60px;width:62px;height:62px;border:3px solid #222"></div>
  <div class="fill" style="left:208px;top:60px;width:62px;height:62px;border:3px solid #222"></div>
  <div class="brand-mark" style="left:10px;top:85px;width:62px;text-align:center;font-size:9px;letter-spacing:0">NORVALE</div>
  <div class="body-text" style="left:78px;top:68px;width:62px;text-align:center;font-size:34px;line-height:44px;font-weight:300;color:#222">2</div>
  <div class="body-text" style="left:10px;top:130px;width:62px;text-align:center;font-size:8px;color:#222">Topic 1</div>
  <div class="body-text" style="left:78px;top:130px;width:62px;text-align:center;font-size:8px;color:#222">Topic 2</div>
  <div class="body-text" style="left:142px;top:130px;width:62px;text-align:center;font-size:8px;color:#222">Topic 3</div>
  <div class="body-text" style="left:208px;top:130px;width:62px;text-align:center;font-size:8px;color:#222">Insert pil's</div>
  <div class="footer" style="color:#333"><span>23-Oct-13</span><span>Confidential</span><span>Presentation name</span><span class="brand">NORVALE</span><span class="page">16</span></div>
</section>

<!-- Agenda list slide -->
<section class="slide" style="left:907px;top:600px">
  <div class="band" style="left:0;top:8px;width:243px;height:19px">agenda</div>
  <div class="body-text" style="left:20px;top:40px;width:255px;font-size:5.5px;line-height:7.5px;text-align:justify">
    <p style="margin-bottom:7px">• In todays presentation we will cover "Structural Aluminium".</p>
    <p style="margin-bottom:7px">• In engineering parlance the term aluminium (or aluminium) covers.</p>
    <p style="margin-bottom:7px">• Any aluminium-based material, and embraces the alloys as well as the pure metal.</p>
    <p style="margin-bottom:7px">• With an annual consumption of 35 million metric tons, aluminium is one of the most commonly used metals globally.</p>
    <p>• Its lightness coupled with its strength, conductivity, barrier properties and its excellent corrosion resistance have all been and continue to be its most important advantages and the main reasons for the continued growth in the usage of aluminium.</p>
  </div>
  <div class="band" style="left:35px;top:156px;width:245px;height:19px"></div>
  <div class="footer"><span>23-Oct-13</span><span>Confidential</span><span>Presentation name</span><span class="brand">NORVALE</span><span class="page">3</span></div>
</section>

<div class="brand-mark" style="left:800px;top:876px;font-size:56px;line-height:62px;letter-spacing:4px">NORVALE</div>

</body>
</html>
```